Packaging Design for Boneless Picnic Ham

We are Tidewell Provisions Limited, a company based in Trinidad which is located within the Caribbean. We produce and sell a plethora of meat products including a variety of hams, sausages and even bacon.

We require a packaging design for a ham product. This product is packaged within a cryovac (11" X 18") shrink bag which would be used to package our Boneless Picnic Ham which weighs 2.5 Kilograms.

The design space should be 7 inches wide and 6 inches in height. The design is 3 inches from the bottom and 2 inches off each side.

Our target audience comprises of caterers as well as the average household folk. What sets our product apart is that it is has a great taste, 20% less salt and is affordable and easy. We commonly refer to it as the "Sunday Roast Joint".

Attached below, is our logo which you must incorporate onto the design. We also request that the header be "Hickory Smoked Boneless Picnic Ham".

Target Market(s)

Caterers and Average Household Folk

Font styles to use
Sans Serif

Requirements
Must have
• The Tidewell Provisions Company Logo and the header must have "Hickory Smoked Boneless Picnic Ham"
Nice to have
• Maximum Creativity
Should not have
• No animal artwork should be included onto the design

```html
<!DOCTYPE html>
<html lang="en">
<head>
<meta charset="utf-8">
<title>Tidewell Provisions – Hickory Smoked Boneless Picnic Ham</title>
<link rel="stylesheet" href="https://fonts.googleapis.com/css2?family=Tinos:wght@400;700&family=Open+Sans:wght@700&display=swap">
<style>
  :root {
    --royal-blue: #2b3d97;
    --gold-light: #e3c45a;
    --gold-mid: #b8962f;
    --gold-dark: #7d6420;
    --banner-yellow: #f6cd16;
    --photo-rim: #f3c300;
    --title-white: #f4f4f4;
    --ink: #2a2a2a;
    --page: #ffffff;
  }
  * { margin: 0; padding: 0; box-sizing: border-box; }
  html, body { width: 1066px; height: 1200px; overflow: hidden; background: var(--page); }
  .label { position: relative; width: 1066px; height: 1200px; }
  .label-shapes { position: absolute; inset: 0; }

  .brand-box {
    position: absolute; left: 343px; top: 73px; width: 380px; height: 196px;
    display: flex; align-items: center; justify-content: center;
  }
  .brand-name {
    font-family: "Tinos", serif; font-weight: 700; font-size: 40px;
    color: var(--royal-blue); text-align: center; line-height: 1.1;
  }

  .product-title {
    position: absolute; left: 0; width: 1066px; top: 318px; text-align: center;
    font-family: "Tinos", serif; font-weight: 700; font-variant: small-caps;
    color: var(--title-white); font-size: 76px; line-height: 92px;
    letter-spacing: 1px; text-shadow: 0 2px 3px rgba(0,0,0,0.35);
  }
  .product-title span { display: block; }

  .claim {
    position: absolute; left: 315px; width: 436px; top: 950px; text-align: center;
    font-family: "Tinos", serif; font-weight: 700; font-size: 44px;
    color: var(--royal-blue); line-height: 60px;
  }
  .claim small { font-variant: small-caps; font-size: 44px; }

  .prep-note {
    position: absolute; left: 0; width: 1066px; top: 1020px; text-align: center;
    font-family: "Tinos", serif; font-variant: small-caps; font-size: 19px;
    line-height: 24px; color: var(--ink);
  }
  .storage {
    position: absolute; left: 0; width: 1066px; top: 1078px; text-align: center;
    font-family: "Open Sans", sans-serif; font-weight: 700; font-size: 23px;
    letter-spacing: 3px; color: var(--royal-blue);
  }
</style>
</head>
<body>
<div class="label">
  <svg class="label-shapes" width="1066" height="1200" viewBox="0 0 1066 1200">
    <defs>
      <linearGradient id="goldFill" x1="0" y1="0" x2="1" y2="0.3">
        <stop offset="0" stop-color="var(--gold-mid)"/>
        <stop offset="0.45" stop-color="var(--gold-light)"/>
        <stop offset="1" stop-color="var(--gold-dark)"/>
      </linearGradient>
      <radialGradient id="hamTones" cx="0.6" cy="0.55" r="0.65">
        <stop offset="0" stop-color="#d89a8c"/>
        <stop offset="0.5" stop-color="#b35a3a"/>
        <stop offset="1" stop-color="#6b4a2a"/>
      </radialGradient>
    </defs>
    <ellipse class="outer-ring" cx="533" cy="598" rx="520" ry="588" fill="var(--royal-blue)"/>
    <ellipse class="gold-field" cx="533" cy="598" rx="492" ry="560" fill="url(#goldFill)"/>

    <rect class="brand-frame" x="343" y="73" width="380" height="196" rx="12" fill="#eef4fb" stroke="var(--royal-blue)" stroke-width="7"/>

    <ellipse class="photo-window" cx="532" cy="735" rx="356" ry="225" fill="url(#hamTones)" stroke="var(--photo-rim)" stroke-width="5" role="img" aria-label="Photo of a glazed clove-studded boneless ham, sliced, on a wooden board with vegetables behind"/>

    <path class="title-ribbon" d="M12 312 C 320 322, 700 282, 1055 312 L 1050 508 C 760 488, 360 560, 38 540 Z" fill="var(--royal-blue)"/>

    <path class="claim-banner" d="M330 955 Q 533 970 738 955 Q 752 955 750 972 L 744 1004 Q 742 1020 728 1020 Q 533 1032 338 1020 Q 324 1020 322 1004 L 316 972 Q 315 955 330 955 Z" fill="var(--banner-yellow)"/>
  </svg>

  <div class="brand-box"><p class="brand-name">Tidewell Provisions</p></div>

  <h1 class="product-title"><span>Hickory Smoked</span><span>Boneless Picnic Ham</span></h1>

  <p class="claim">20% <small>Less Salt</small></p>

  <p class="prep-note">Hickory Smokes &amp; Fully Cooked<br>Water Added</p>

  <p class="storage">KEEP REFRIGERATED</p>
</div>
</body>
</html>
```